creative pack design with extended budget for Velmoraq coffee product

- we need a packing design for a new product of coffee for our company Tesmo Kirul located in Uganda.
- specialty Arabica coffee grown at slopes of Mountain Elgon with rich volcanic soils located in Eastern region of Uganda.
-  we have a logo already made and has registered in Uganda. our logo colors are mixture between a lot of brown color and yellow. vacuum  plastic bags.
- there is no restrictions towards your imagination .
-  all details available
- we will launch our product through phases ;
- phase 1 is  a ground coffee : ( Turkish coffee )  2 degrees of roasting which are ( medium dark , light ) of 250 grm
b) roasted beans: 2 degrees ( medium, dark) of 250 grm & 1000 grm
- we need also to highlight the eastern spirit of Turkish coffee
- we  need designs, the info and color only will be changed depending on previous classifications

Target Market(s)
Arab countries, Turkey , Uganda, Europe
Colors
Designer to choose colors to be used in the design.
Requirements
Nice to have
- about nature , Elgon mountain , farmers, freshness, distinctive product, soul of east such as decorated cup of Turkish coffee . these just an ideas but there is no restrictions on your imagination

```html
<!DOCTYPE html>
<html lang="en">
<head>
<meta charset="utf-8">
<title>Velmoraq Turkish Ground Coffee – Pack Fronts</title>
<link rel="stylesheet" href="https://fonts.googleapis.com/css2?family=Marcellus&family=Alegreya+Sans:wght@400;500&display=swap">
<style>
  :root {
    --backdrop: #ecebe5;
    --bag-black: #141414;
    --parchment-core: #f8ecd3;
    --parchment-mid: #f0d7ab;
    --parchment-edge: #e4a682;
    --ink: #1c1612;
    --logo-brown: #5a2e1c;
    --dark-roast: #34260f;
    --dark-roast-band: #3b2a12;
    --light-roast: #c97f4f;
    --light-roast-band: #d49468;
    --light-roast-top: #d8926a;
    --band-text: #f3e6d2;
  }
  * { box-sizing: border-box; margin: 0; padding: 0; }
  html, body { width: 1200px; height: 784px; overflow: hidden; }
  body {
    background: var(--backdrop);
    font-family: "Marcellus", serif;
    color: var(--ink);
  }
  .pack-range {
    position: relative;
    width: 1200px;
    height: 784px;
    display: flex;
    justify-content: center;
    align-items: center;
    gap: 104px;
  }
  .pack {
    width: 320px;
    height: 500px;
    background: var(--bag-black);
    border-radius: 10px;
    padding: 12px 14px 14px;
    display: flex;
    flex-direction: column;
  }
  .pack__top-band { height: 40px; border-radius: 8px 8px 0 0; }
  .pack__label {
    flex: 1;
    background: radial-gradient(ellipse at 50% 45%, var(--parchment-core) 0%, var(--parchment-mid) 62%, var(--parchment-edge) 100%);
    display: flex;
    flex-direction: column;
    align-items: center;
    padding-top: 14px;
  }
  .brand {
    display: flex;
    flex-direction: column;
    align-items: center;
    gap: 4px;
  }
  .brand__disc {
    width: 58px; height: 58px;
    border-radius: 50%;
    background: var(--logo-brown);
  }
  .brand__name {
    font-family: "Marcellus", serif;
    font-size: 21px;
    line-height: 24px;
    letter-spacing: 1px;
    color: var(--logo-brown);
  }
  .skyline-art {
    margin-top: 12px;
    width: 172px;
    height: 140px;
  }
  .pack--medium-dark .skyline-art {
    background: radial-gradient(ellipse 50% 50% at 50% 60%, rgba(40,30,20,0.42) 0%, rgba(40,30,20,0.22) 55%, rgba(40,30,20,0) 100%);
  }
  .pack--light .skyline-art {
    background: radial-gradient(ellipse 50% 50% at 50% 60%, rgba(196,112,62,0.5) 0%, rgba(196,112,62,0.25) 55%, rgba(196,112,62,0) 100%);
  }
  .roast-bubble {
    position: relative;
    margin-top: 8px;
    height: 42px;
    width: 124px;
    border-radius: 9px;
    display: flex;
    align-items: center;
    justify-content: center;
    font-family: "Alegreya Sans", sans-serif;
    color: var(--band-text);
    line-height: 1;
  }
  .roast-bubble::after {
    content: "";
    position: absolute;
    left: 50%;
    bottom: -12px;
    transform: translateX(-6px);
    border-left: 10px solid transparent;
    border-top: 13px solid var(--bubble-colour);
  }
  .pack--medium-dark .roast-bubble { --bubble-colour: var(--dark-roast); background: var(--dark-roast); font-size: 17px; }
  .pack--light .roast-bubble { --bubble-colour: var(--light-roast); background: var(--light-roast); font-size: 26px; width: 126px; }
  .product-title {
    margin-top: 24px;
    text-align: center;
    font-weight: 400;
    font-size: 21px;
    line-height: 20px;
    letter-spacing: 0.5px;
  }
  .pack__net {
    height: 40px;
    display: flex;
    align-items: center;
    justify-content: center;
    font-family: "Alegreya Sans", sans-serif;
    font-size: 14px;
    color: var(--band-text);
    border-radius: 0 0 8px 8px;
  }
  .pack--medium-dark .pack__top-band { background: var(--dark-roast-band); }
  .pack--medium-dark .pack__net { background: var(--dark-roast-band); }
  .pack--light .pack__top-band { background: var(--light-roast-top); }
  .pack--light .pack__net { background: var(--light-roast-band); }
</style>
</head>
<body>
  <main class="pack-range">
    <article class="pack pack--medium-dark">
      <div class="pack__top-band"></div>
      <div class="pack__label">
        <div class="brand">
          <span class="brand__disc"></span>
          <span class="brand__name">Velmoraq</span>
        </div>
        <div class="skyline-art" role="img" aria-label="Ink sketch of an Eastern mosque skyline with domes, minarets, stars and a crescent moon"></div>
        <div class="roast-bubble">medium dark</div>
        <h1 class="product-title">TURKISH<br>GROUND COFFEE</h1>
      </div>
      <div class="pack__net">Net 250 grm</div>
    </article>

    <article class="pack pack--light">
      <div class="pack__top-band"></div>
      <div class="pack__label">
        <div class="brand">
          <span class="brand__disc"></span>
          <span class="brand__name">Velmoraq</span>
        </div>
        <div class="skyline-art" role="img" aria-label="Copper-toned sketch of an Eastern mosque skyline with domes, minarets, stars and a crescent moon"></div>
        <div class="roast-bubble">light</div>
        <h1 class="product-title">TURKISH<br>GROUND COFFEE</h1>
      </div>
      <div class="pack__net">Net 250 grm</div>
    </article>
  </main>
</body>
</html>
```